We Need a GREAT Looking Sales Flyer!

Our small, boutique fitness facility needs a new flyer which highlights a new entry level fitness program that we are launching.

The flyer should be visually appealing as we will be handing a full color version to the potential member during our sales process.

I have attached:
- a word document which includes text
-Photos that can be used. Not all need to be used. These are to be used as you feel appropriate
- Our Logo

```html
<!DOCTYPE html>
<html lang="en">
<head>
<meta charset="utf-8">
<title>StrideForge – The Ultimate Kickstart</title>
<link rel="stylesheet" href="https://fonts.googleapis.com/css2?family=Bebas+Neue&family=Montserrat:wght@300;400;500;700;800&display=swap">
<style>
  :root {
    --backdrop: #d4d4d6;
    --ink: #050505;
    --paper-text: #e4e4ea;
    --soft-text: #d6d6dc;
    --yellow: #e0b80f;
    --blue: #1466b8;
    --blue-band: #1a6fc0;
    --photo-dark: #17386e;
    --photo-light: #3a72bd;
    --strike: #d21f2a;
  }
  * { margin: 0; padding: 0; box-sizing: border-box; }
  html, body { width: 1135px; height: 1200px; overflow: hidden; background: var(--backdrop); }
  .stage { position: relative; width: 1135px; height: 1200px; }
  .flyer {
    position: absolute; left: 128px; top: 22px;
    width: 788px; height: 1035px;
    transform: scale(1.117); transform-origin: 0 0;
    background: var(--ink); overflow: hidden;
    font-family: "Montserrat", sans-serif; color: var(--paper-text);
  }
  .hero-shape { position: absolute; left: 0; top: 0; width: 788px; height: 1035px; }
  .headline-top {
    position: absolute; left: 57px; top: 92px;
    font-family: "Bebas Neue", sans-serif; font-size: 78px; line-height: 1;
    color: var(--paper-text); letter-spacing: 0.5px;
  }
  .headline-now {
    position: absolute; left: 52px; top: 162px;
    font-family: "Montserrat", sans-serif; font-weight: 800; font-size: 162px;
    line-height: 1; color: var(--yellow); letter-spacing: -4px;
  }
  .program-kicker {
    position: absolute; left: 57px; top: 360px;
    font-weight: 300; font-size: 25px; letter-spacing: 3px; color: var(--paper-text);
  }
  .program-name {
    position: absolute; left: 55px; top: 390px;
    font-weight: 300; font-size: 55px; line-height: 1.1; color: var(--paper-text);
  }
  .benefits-title {
    position: absolute; left: 57px; top: 492px;
    font-weight: 800; font-size: 38px; line-height: 52px; color: var(--blue);
  }
  .benefits {
    position: absolute; left: 55px; top: 610px; width: 320px; list-style: none;
  }
  .benefits li {
    position: relative; padding-left: 20px; margin-bottom: 17px;
    font-size: 14.5px; line-height: 18px; font-weight: 400; color: var(--soft-text);
  }
  .benefits li svg { position: absolute; left: 0; top: 4px; width: 12px; height: 12px; }
  .divider { position: absolute; left: 428px; top: 607px; width: 1px; height: 313px; background: #6a6a6a; }
  .promise {
    position: absolute; right: 60px; top: 655px; text-align: right;
    font-weight: 400; font-size: 29px; line-height: 41px; color: var(--paper-text);
  }
  .offer-band {
    position: absolute; left: 502px; top: 792px; width: 226px; height: 26px;
    background: var(--yellow); color: var(--ink);
    font-weight: 500; font-size: 17px; letter-spacing: 3.4px; line-height: 26px; text-align: center;
  }
  .price-old, .price-new {
    position: absolute; top: 822px; font-weight: 400; font-size: 52px; line-height: 60px; color: var(--paper-text);
  }
  .price-old { left: 498px; }
  .price-new { left: 636px; }
  .price-strike { position: absolute; left: 500px; top: 836px; width: 118px; height: 44px; }
  .price-note { position: absolute; right: 66px; top: 880px; font-size: 11px; color: var(--paper-text); }
  .website { position: absolute; left: 57px; top: 958px; font-size: 30px; font-weight: 400; color: var(--paper-text); }
  .brand {
    position: absolute; right: 58px; top: 940px;
    font-weight: 800; font-size: 42px; letter-spacing: -1px; color: var(--paper-text);
  }
</style>
</head>
<body>
<div class="stage">
  <main class="flyer">
    <svg class="hero-shape" viewBox="0 0 788 1035" aria-hidden="false">
      <defs>
        <linearGradient id="photoTone" x1="0" y1="0" x2="1" y2="1">
          <stop offset="0" stop-color="var(--photo-light)"/>
          <stop offset="0.55" stop-color="#2a5ca3"/>
          <stop offset="1" stop-color="var(--photo-dark)"/>
        </linearGradient>
      </defs>
      <path fill="var(--blue-band)" d="M330 0 H788 V606 C760 612 735 600 722 590 C690 565 650 580 620 550 C590 520 560 500 525 485 C480 460 470 420 440 395 C415 372 420 340 405 300 C395 270 380 230 340 180 C300 130 290 60 318 22 Z"/>
      <g role="img" aria-label="Photo of a smiling group of members and trainers posing together in the gym">
        <path fill="url(#photoTone)" d="M340 0 H788 V590 C760 592 742 580 725 568 C695 548 660 555 628 528 C598 503 570 488 535 470 C495 450 485 412 455 385 C432 362 435 330 420 295 C408 265 392 225 355 178 C318 130 305 62 330 22 Z"/>
      </g>
    </svg>

    <h1 class="headline-top">CHANGE BEGINS</h1>
    <div class="headline-now">NOW!</div>

    <p class="program-kicker">THE ULTIMATE</p>
    <h2 class="program-name">KICKSTART</h2>

    <h3 class="benefits-title">WHAT<br>YOU GET</h3>
    <ul class="benefits">
      <li><svg viewBox="0 0 12 12"><circle cx="6" cy="6" r="4.8" fill="none" stroke="#e0b80f" stroke-width="1.4"/><path d="M3.6 6.1 L5.4 7.8 L10.6 2.4" fill="none" stroke="#e0b80f" stroke-width="1.6"/></svg>Unlimited Group Training Designed Specifically to Sculpt &amp; Tone the body.</li>
      <li><svg viewBox="0 0 12 12"><circle cx="6" cy="6" r="4.8" fill="none" stroke="#e0b80f" stroke-width="1.4"/><path d="M3.6 6.1 L5.4 7.8 L10.6 2.4" fill="none" stroke="#e0b80f" stroke-width="1.6"/></svg>CUSTOM Meal Plan designed specifically for Your and Your Body Type</li>
      <li><svg viewBox="0 0 12 12"><circle cx="6" cy="6" r="4.8" fill="none" stroke="#e0b80f" stroke-width="1.4"/><path d="M3.6 6.1 L5.4 7.8 L10.6 2.4" fill="none" stroke="#e0b80f" stroke-width="1.6"/></svg>Detailed Body Scans to track results</li>
      <li><svg viewBox="0 0 12 12"><circle cx="6" cy="6" r="4.8" fill="none" stroke="#e0b80f" stroke-width="1.4"/><path d="M3.6 6.1 L5.4 7.8 L10.6 2.4" fill="none" stroke="#e0b80f" stroke-width="1.6"/></svg>Supplement List to accelerate metabolism</li>
      <li><svg viewBox="0 0 12 12"><circle cx="6" cy="6" r="4.8" fill="none" stroke="#e0b80f" stroke-width="1.4"/><path d="M3.6 6.1 L5.4 7.8 L10.6 2.4" fill="none" stroke="#e0b80f" stroke-width="1.6"/></svg>10% off First Supplement Purchase to Kickstart the process</li>
      <li><svg viewBox="0 0 12 12"><circle cx="6" cy="6" r="4.8" fill="none" stroke="#e0b80f" stroke-width="1.4"/><path d="M3.6 6.1 L5.4 7.8 L10.6 2.4" fill="none" stroke="#e0b80f" stroke-width="1.6"/></svg>Exclusive access to StrideForge’s Private Circlehub Page for additional recipes, Support and Guidance</li>
    </ul>

    <div class="divider"></div>

    <p class="promise">The Life That<br>You Envision IS<br>POSSIBLE!</p>
    <div class="offer-band">GET STARTED FOR</div>
    <span class="price-old">$199</span>
    <svg class="price-strike" viewBox="0 0 118 44"><path d="M4 40 L114 6 M8 8 L112 40" stroke="var(--strike)" stroke-width="3" fill="none"/></svg>
    <span class="price-new">$99</span>
    <span class="price-note">for limited time</span>

    <p class="website">www.strideforge.com</p>
    <div class="brand">StrideForge</div>
  </main>
</div>
</body>
</html>
```